Plakat für Hausverwaltung
Zielgruppe
Hausverwaltung
(Verwaltung von Wohn- und Gewerbeimmobilien)
Aufgabenstellung
Es soll ein Werbeplakat werden, Die Inhalte der Dienstleistung und die Firmenfarben kann der Webseite entnommen werden.
Ein guter Werbespruch und ansprechendes Desing ohne viel Schrift.

```html
<!DOCTYPE html>
<html lang="de">
<head>
<meta charset="utf-8">
<title>KORVAN Hausverwaltung – Banner</title>
<link rel="stylesheet" href="https://fonts.googleapis.com/css2?family=Montserrat:wght@400;500;600&family=Saira+Extra+Condensed:wght@400&family=Tinos&family=Roboto:wght@400&display=swap">
<style>
  :root{
    --stage:#c4c4c6;
    --light-top:#e2dfdb;
    --light-bottom:#d2ccc5;
    --headline:#4b4037;
    --ink:#2a2a2a;
    --dark:#1d1d1d;
    --dark-text:#e6e4e1;
    --accent:#8c7b69;
    --accent-light:#b3a08a;
    --muted:#a59886;
  }
  *{box-sizing:border-box;margin:0;padding:0}
  html,body{width:1200px;height:900px;overflow:hidden}
  body{background:var(--stage);position:relative;font-family:'Montserrat',sans-serif}
  .banner{position:absolute;left:40px;top:168px;width:1120px;height:564px;overflow:hidden;background:var(--dark);box-shadow:0 6px 18px rgba(0,0,0,.18)}
  .intro{position:absolute;left:0;top:0;width:1120px;height:288px;background:linear-gradient(180deg,var(--light-top),var(--light-bottom))}
  .team-photo{position:absolute;right:0;top:0;width:565px;height:288px;background:linear-gradient(90deg,#d5cfc8 0%,#cfc8c0 40%,#c2bbb3 100%)}
  .brand{position:absolute;left:121px;top:30px;display:flex;align-items:center;gap:10px}
  .brand-name{font-family:'Montserrat',sans-serif;font-weight:500;font-size:30px;letter-spacing:8px;color:var(--ink)}
  .brand-mark{width:30px;height:30px;border:2px solid var(--ink)}
  .brand-sub{position:absolute;left:28px;top:70px;font-family:'Tinos',serif;font-size:18px;color:var(--ink)}
  .headline{position:absolute;left:28px;top:108px;font-family:'Saira Extra Condensed',sans-serif;font-weight:400;font-size:54px;line-height:54px;color:var(--headline)}
  .divider{position:absolute;left:0;top:233px;width:501px;height:1px;background:var(--headline)}
  .features{position:absolute;left:0;top:248px;width:560px;height:34px}
  .feature{position:absolute;top:0;display:flex;align-items:center;gap:8px;font-family:'Roboto',sans-serif;font-size:9px;line-height:11px;color:var(--ink)}
  .feature svg{width:26px;height:28px;stroke:var(--ink);fill:none;stroke-width:1.2}
  .offers{position:absolute;left:0;top:288px;width:1120px;height:276px;background:var(--dark);color:var(--dark-text)}
  .offers-tab{position:absolute;left:0;top:2px;width:240px;height:25px;background:var(--accent);clip-path:polygon(0 0,100% 0,93% 100%,0 100%);font-weight:500;font-size:17px;line-height:25px;padding-left:24px;color:var(--dark)}
  .offer{position:absolute;top:40px}
  .offer-title{display:flex;align-items:center;gap:8px;font-weight:500;font-size:15px;color:#fff}
  .offer-num{width:20px;height:20px;border-radius:50%;background:var(--accent);color:var(--dark);font-size:10px;display:flex;align-items:center;justify-content:center}
  .offer ul{list-style:none;margin:8px 0 0 28px;font-size:11px;line-height:13.8px}
  .offer li::before{content:"▪ ";font-size:8px}
  .offer-1{left:24px}.offer-2{left:495px}.offer-3{left:859px}
  .contact{position:absolute;left:941px;top:150px;font-size:10.5px;line-height:13px;color:var(--muted)}
  .contact-row{display:flex;gap:8px;align-items:flex-start;margin-bottom:9px}
  .contact-row svg{width:14px;height:13px;stroke:var(--muted);fill:none;stroke-width:1.2;flex:none}
  .web{position:absolute;left:902px;top:232px;width:218px;height:20px;background:var(--accent-light);clip-path:polygon(7% 0,100% 0,100% 100%,0 100%);font-size:11px;line-height:20px;text-align:center;color:var(--dark)}
  .web strong{font-weight:600}
</style>
</head>
<body>
  <section class="banner">
    <div class="intro">
      <div class="team-photo" role="img" aria-label="Teamfoto: drei Mitarbeitende vor einem Aktenregal"></div>
      <div class="brand"><span class="brand-name">KORVAN</span><span class="brand-mark"></span></div>
      <p class="brand-sub">Haus- und Grundstücksverwaltungs GmbH</p>
      <h1 class="headline">Herzlich willkommen bei Ihrer<br>Hausverwaltung im Raum Marburg</h1>
      <div class="divider"></div>
      <div class="features">
        <div class="feature" style="left:32px"><svg viewBox="0 0 26 28"><path d="M2 14 13 3l11 11M5 11v15h16V11"/></svg><span>Fachliche<br>Erfahrung</span></div>
        <div class="feature" style="left:134px"><svg viewBox="0 0 26 28"><rect x="2" y="3" width="22" height="22"/><path d="M13 3v22M2 14h22"/></svg><span>Professionelle<br>Beratung</span></div>
        <div class="feature" style="left:257px"><svg viewBox="0 0 26 28"><circle cx="7" cy="8" r="3"/><circle cx="13" cy="5" r="3"/><circle cx="19" cy="8" r="3"/><path d="M3 22c0-6 20-6 20 0"/></svg><span>Junges und<br>engagiertes Team</span></div>
        <div class="feature" style="left:395px"><svg viewBox="0 0 26 28"><path d="M2 5h22M4 8h18M6 8v15M11 8v15M15 8v15M20 8v15M3 24h20"/></svg><span>Zukunftsfähig &amp;<br>Verantwortungsbewusst</span></div>
      </div>
    </div>

    <div class="offers">
      <div class="offers-tab">Unsere Angebote:</div>

      <div class="offer offer-1">
        <h2 class="offer-title"><span class="offer-num">1</span>Sondereigentumsverwaltung</h2>
        <ul>
          <li>Direkte Vertretung des Eigentümers gegenüber den Mietern</li>
          <li>Durchführung des gesamten Schriftverkehrs</li>
          <li>Vermietung über anerkannte Makler mit Bonitätsprüfung</li>
          <li>Ausarbeitung und Abschluss erprobter Mietverträge</li>
          <li>Durchführung der Wohnungsübergaben</li>
          <li>Überwachung der Miethöhe und Durchführung von Mietanpassungen</li>
          <li>Überwachung der Zahlungseingänge</li>
          <li>Durchführung des gesamten Zahlungsverkehr und Führen Ihres Mietkontos</li>
          <li>Erfassen der Ein- und Ausgaben</li>
          <li>Abrechnung aller Nebenkosten mit den Mietern</li>
          <li>Verwaltung der Mietkautionen</li>
          <li>Erstellung der jährlichen Gesamtabrechnung für den Eigentümer</li>
          <li>Veranlassen notwendiger Reparaturen und Erhaltungsmaßnahmen</li>
          <li>Einleitung von Sofortmaßnahmen in Notfällen.</li>
        </ul>
      </div>

      <div class="offer offer-2">
        <h2 class="offer-title"><span class="offer-num">2</span>Wohneigentumsverwaltung</h2>
        <ul>
          <li>Verwaltung der gemeinschaftlichen Angelegenheiten</li>
          <li>Erstellung des Wirtschaftsplans</li>
          <li>Erstellung der Jahresberechnung</li>
          <li>Eigentümerversammlung und Niederschrift</li>
          <li>Verwaltung der gemeinschaftlichen Gelder</li>
          <li>Überwachen der Verträge der Gemeinschaft</li>
          <li>Zahlungsverkehr und Buchführung</li>
          <li>Auftragsvergabe gemäß Beschlussfassung</li>
          <li>Sofortmaßnahmen bei dringenden Schadensfällen</li>
          <li>Technische Betreuung des Gemeinschaftseigentums</li>
          <li>Sicherheitseinrichtungen</li>
          <li>Allgemeine Verwaltung mit Behörden und Eigentümern</li>
        </ul>
      </div>

      <div class="offer offer-3">
        <h2 class="offer-title"><span class="offer-num">3</span>Mietverwaltung</h2>
        <ul>
          <li>Allgemeine Verwaltung</li>
          <li>Kaufmännische Verwaltung</li>
          <li>Technische Betreuung</li>
          <li>Nebenkostenabrechnungsservice</li>
        </ul>
      </div>

      <div class="contact">
        <div class="contact-row"><svg viewBox="0 0 14 13"><path d="M1 6 7 1l6 5M3 5v7h8V5"/></svg><span>Lindenweg 12<br>35039 Marburg</span></div>
        <div class="contact-row"><svg viewBox="0 0 14 13"><rect x="1" y="2.5" width="12" height="8"/><path d="m1 3 6 4 6-4"/></svg><span>info@korvan-marburg.de</span></div>
        <div class="contact-row"><svg viewBox="0 0 14 13"><rect x="4" y="0.5" width="6" height="12" rx="1"/></svg><span>06421 555019</span></div>
      </div>

      <div class="web">www.<strong>KORVAN-MARBURG</strong>.de</div>
    </div>
  </section>
</body>
</html>
```